Dental Magazine Cover

I need a template created for a magazine cover. Magazine title is "Dentistry Halvern"

I would like to have a logo designed for "Dentistry Halvern"

For each issue, we would like to keep the same basic template and change out the photos, text, etc. according to the contents of the issue.

You can create the cover of the first issue with the attached photos and captions:

Date for use on magazine cover is February 2014

Main caption: Maxillary Reconstruction with Immediately Loaded Dental Implants
(Use attached File 1 for main photo. Photo may be cropped and rotated as needed)

Inset: Bisphosphonate Guidelines for Dental Treatment
(Use attached file 2 for inset photo. Photo may be cropped and rotated as needed).

Target Market(s)

Target audience for this magazine are dentists, dental hygienists, dental assistants, and dental professionals in the Austin, Texas area.

Industry/Entity Type

Dental

Other font styles liked:
• Font need to "POP"

Requirements
Must have
• Please see project overview guidelines. Magazine cover needs to have the following:
1) Logo
2) Main image
3) Caption for Main image (Maxillary Reconstruction with Immediately Loaded Dental Implants)
4) Smaller Inset Photo
5) Caption for smaller inset photo (Bisphosphonate Guidelines for Dental Treatment)
6) Date of magazine issue (February 2014)

Use any of the Photos you see fit to make the magazine cover work.
Nice to have
• Please try to make the "Dentistry Halvern" logo "POP". Dental journals are boring enough. We can at least have a logo that pops. Simply using generic text will win this design. The below text is just a suggestion of a Logo. Please feel free to use all creative license in making a logo that has some sizzle. PLEASE NOTE: A tooth is NOT needed in the logo...

```html
<!DOCTYPE html>
<html lang="en">
<head>
<meta charset="utf-8">
<title>Dentistry Halvern — February 2014</title>
<link rel="stylesheet" href="https://fonts.googleapis.com/css2?family=Comfortaa:wght@400;600&display=swap">
<style>
  :root {
    --page-bg: #ececec;
    --sky-light: #22b4ee;
    --sky-mid: #1b7fd4;
    --royal: #1a3d9e;
    --navy: #0d2473;
    --navy-deep: #0a1a5c;
    --teal: #2bb3c6;
    --caption-cyan: #45d2f2;
    --caption-orange: #f7a01c;
    --white: #ffffff;
  }
  * { box-sizing: border-box; margin: 0; padding: 0; }
  html, body {
    width: 1200px; height: 900px; overflow: hidden;
    background: var(--page-bg);
  }
  .cover {
    position: absolute; left: 290px; top: 55px;
    width: 620px; height: 790px;
    overflow: hidden;
    background: linear-gradient(180deg, var(--royal) 0%, var(--navy) 70%, var(--navy-deep) 100%);
    font-family: "Comfortaa", sans-serif;
  }
  .masthead {
    position: absolute; left: 0; top: 0; width: 620px; height: 214px;
    background: linear-gradient(200deg, var(--sky-light) 0%, var(--sky-mid) 40%, var(--royal) 100%);
  }
  .masthead__title { position: absolute; left: 0; top: 30px; width: 620px; text-align: center; color: var(--white); font-weight: 400; }
  .masthead__kicker { display: block; font-size: 42px; letter-spacing: 1px; margin-left: -40px; }
  .masthead__name { display: block; font-size: 104px; line-height: 1.05; letter-spacing: 2px; }
  .issue-date {
    position: absolute; right: 0; top: 189px; height: 25px; width: 285px;
    color: var(--white); font-size: 15px; line-height: 25px;
    text-align: right; padding-right: 28px;
  }
  .issue-date svg { position: absolute; left: 0; top: 0; z-index: -1; }
  .feature-photo {
    position: absolute; left: 0; top: 214px; width: 620px; height: 376px;
    background:
      radial-gradient(ellipse at 20% 40%, rgba(120,200,90,.55), transparent 45%),
      radial-gradient(ellipse at 70% 30%, rgba(200,90,200,.5), transparent 45%),
      radial-gradient(ellipse at 50% 70%, rgba(230,220,180,.45), transparent 50%),
      #111018;
  }
  .inset {
    position: absolute;
    border: 3px solid var(--teal);
  }
  .inset--main {
    left: 181px; top: 474px; width: 186px; height: 118px;
    background: linear-gradient(180deg, #b9ac8e 0%, #7fc9a2 55%, #3a3a32 100%);
  }
  .inset--secondary {
    left: 405px; top: 496px; width: 192px; height: 96px;
    background: linear-gradient(180deg, #3a2a20 0%, #c9a888 50%, #6a4a38 100%);
    clip-path: polygon(14% 0, 100% 0, 100% 100%, 0 100%, 0 22%);
  }
  .caption {
    position: absolute; font-size: 19px; line-height: 27px; font-weight: 400;
  }
  .caption--main { left: 195px; top: 610px; width: 200px; color: var(--caption-cyan); text-align: center; }
  .caption--secondary { left: 418px; top: 612px; width: 170px; color: var(--caption-orange); }
</style>
</head>
<body>
  <main class="cover">
    <header class="masthead">
      <h1 class="masthead__title">
        <span class="masthead__kicker">Dentistry</span>
        <span class="masthead__name">Halvern</span>
      </h1>
    </header>

    <div class="issue-date">
      <svg width="285" height="25" viewBox="0 0 285 25" aria-hidden="true">
        <polygon points="14,0 285,0 285,25 0,25" fill="var(--teal)"/>
      </svg>
      February 2014
    </div>

    <div class="feature-photo" role="img" aria-label="Colourful micro-CT scan of trabecular bone structure"></div>
    <div class="inset inset--main" role="img" aria-label="Dental model with implant-supported maxillary reconstruction"></div>
    <div class="inset inset--secondary" role="img" aria-label="Close-up of a dental prosthesis on a model"></div>

    <p class="caption caption--main">Maxillary Reconstruction with Immediately Loaded Dental Implants</p>
    <p class="caption caption--secondary">Bisphosphonate Guidelines for Dental Treatment</p>
  </main>
</body>
</html>
```